redesign of web page www.rosaandtedsroamingfarm.com

id like you to redesign our web page fresh new look using our icons and pics on page and ones I will upload can use wording from web page we are a mobile zoo that comes to your location for birthdays and also public events if we could have few pages one that is for birthdays one for events and one for animal removal we are fully licensed for native and pest animal relocation we use Linux hosting Dreamweaver upload
we do school fetes kindergartens aged care disability and more our web page now
www.rosaandtedsroamingfarm.com

Target Market(s)

public events schools kindergartens aged care

Number of Pages Required

1 page

Font styles to use
Script

Requirements
Must have
• that we have full range of native animals to interact with and learn about or grate wildlife face book link https://www.facebook.com/RosaAndTedsRoamingFarm/
• can use photos of page
• and donation link as well

```html
<!DOCTYPE html>
<html lang="en">
<head>
<meta charset="utf-8">
<title>Rosa &amp; Ted's Roaming Farm</title>
<link href="https://fonts.googleapis.com/css2?family=Fjalla+One&family=Patrick+Hand&display=swap" rel="stylesheet">
<style>
:root{
  --teal:#12806a;
  --teal-dark:#0c6654;
  --heading:#138064;
  --lime:#c6d630;
  --lime-dark:#a9b91c;
  --leaf:#4f9a3c;
  --ink:#333333;
  --muted:#666666;
  --paper:#ffffff;
  --night:#1b1b1b;
  --hand:"Patrick Hand", cursive;
  --bold:"Fjalla One", sans-serif;
}
*{box-sizing:border-box;margin:0;padding:0}
html,body{width:1200px;height:4055px;overflow:hidden}
body{background:var(--paper);font-family:var(--hand);color:var(--ink);position:relative}
a{color:inherit;text-decoration:none}

.topbar{position:absolute;top:10px;right:110px;font-family:var(--bold);font-size:14px;color:#c9c9c9;display:flex;align-items:center;gap:8px}
.brand{position:absolute;top:110px;left:0;width:1200px;display:flex;justify-content:center;align-items:center;gap:16px}
.brand-mark{width:62px;height:62px;border-radius:50%;background:var(--leaf)}
.brand-name{font-family:var(--bold);font-size:50px;color:var(--teal);line-height:1}

.mainnav{position:absolute;top:273px;left:0;width:1200px;height:63px;background:var(--teal)}
.mainnav ul{list-style:none;display:flex;position:absolute;left:245px;top:0;height:63px}
.mainnav li{font-family:var(--bold);font-size:20px;color:#fff;padding:0 19px;line-height:63px}
.mainnav li.is-active{background:#1fa088;position:relative;top:-8px;line-height:79px;height:71px}

.hero{position:absolute;top:336px;left:0;width:1200px;height:537px}
.hero-photo{position:absolute;inset:0;background:linear-gradient(100deg,#3d4a3a 0%,#8f9a8e 30%,#d6dad6 55%,#b9c2bb 75%,#3b4d37 100%)}
.hero-copy{position:absolute;left:212px;top:52px;width:460px;text-align:center}
.hero-title{font-family:var(--hand);font-size:56px;line-height:58px;color:#fff;letter-spacing:2px}
.hero-text{margin-top:20px;font-size:20px;line-height:23px;color:#f1ec2c;text-align:justify}
.btn{display:inline-block;background:var(--lime);color:#1f2a10;font-family:var(--bold);text-align:center}
.hero .btn{position:absolute;left:93px;top:400px;width:251px;height:44px;line-height:44px;font-size:20px}
.dots{position:absolute;left:566px;top:488px;display:flex;gap:10px}
.dots span{width:13px;height:13px;border-radius:50%;background:rgba(255,255,255,.55)}
.dots span:first-child{background:#fff}

.section-title{position:absolute;left:0;width:1200px;text-align:center;font-family:var(--bold);font-size:44px;color:var(--heading);font-weight:400}
.section-title::after{content:"";display:block;width:60px;height:4px;background:var(--lime);margin:6px auto 0}
.section-lead{position:absolute;left:70px;width:1060px;text-align:center;font-size:20px;line-height:26px;color:var(--muted)}

.story-grid{position:absolute;top:1096px;left:60px;width:1080px;height:546px;display:grid;grid-template-columns:repeat(4,270px);grid-template-rows:273px 273px}
.story-photo{width:270px;height:273px}
.story-text{padding:18px 22px;font-size:14.5px;line-height:17px;text-align:center;color:#2a6a2a;display:flex;align-items:center}

.donate-band{position:absolute;top:1645px;left:0;width:1200px;height:200px;background:var(--leaf);text-align:center}
.donate-band p{padding:10px 70px 0;font-size:22px;line-height:24px;color:#fff;text-transform:uppercase}
.donate-band .btn{margin-top:10px;width:260px;height:46px;line-height:46px;font-size:26px}
.pay-row{display:flex;justify-content:center;gap:8px;margin-top:8px}
.pay-row span{width:30px;height:20px;border-radius:3px;background:#fff;opacity:.85}

.slider-arrows{position:absolute;top:2022px;left:1060px;display:flex;gap:6px}
.slider-arrows span{width:32px;height:24px;background:var(--leaf);display:flex;align-items:center;justify-content:center}

.animal-grid{position:absolute;top:2056px;left:74px;display:grid;grid-template-columns:repeat(4,245px);gap:27px 25px}
.animal-card{position:relative;width:245px;height:247px}
.animal-card .shade{position:absolute;inset:0;background:linear-gradient(180deg,rgba(0,0,0,0) 35%,rgba(0,0,0,.55) 100%)}
.animal-name{position:absolute;left:0;right:0;bottom:50px;text-align:center;font-family:var(--bold);font-size:19px;line-height:21px;color:#fff}
.animal-card .btn{position:absolute;left:62px;bottom:14px;width:121px;height:24px;line-height:24px;font-size:13px}

.service-list{position:absolute;top:2818px;left:160px;width:880px;display:flex;justify-content:space-between}
.service{width:200px;text-align:center}
.service svg{display:block;margin:0 auto}
.service h3{font-family:var(--bold);font-size:18px;line-height:20px;color:var(--heading);margin-top:12px;font-weight:400}
.service p{font-size:12px;line-height:13px;color:var(--muted);margin-top:6px}
.service .btn{margin-top:12px;width:150px;height:26px;line-height:26px;font-size:13px}

.contact{position:absolute;top:3084px;left:0;width:1200px;height:638px}
.contact-photo{position:absolute;inset:0;background:linear-gradient(90deg,#2b2a26 0%,#6b5a4c 20%,#3a3a35 45%,#4a4c44 70%,#2a2b28 100%)}
.contact-panel{position:absolute;left:387px;top:52px;width:426px;height:490px;background:rgba(35,110,40,.55);padding:20px 26px}
.contact-panel h2{font-family:var(--bold);font-size:40px;color:var(--lime);text-align:center;font-weight:400}
.field{margin-top:12px;height:44px;border:2px solid #e9e9e9;color:#eee;font-size:17px;padding:8px 10px;display:flex;justify-content:space-between}
.field.message{height:118px}
.note{font-size:11px;color:#eee;margin-top:6px}
.contact-panel .btn{display:block;margin:14px auto 0;width:152px;height:38px;line-height:38px;font-size:20px}

.site-footer{position:absolute;top:3722px;left:0;width:1200px;height:333px;background:var(--night)}
.social{position:absolute;top:95px;left:392px;display:flex;gap:72px}
.social-link{width:88px;height:88px;border-radius:50%;border:3px solid;display:flex;align-items:center;justify-content:center;font-family:var(--bold);font-size:15px}
.social-page{border-color:#2b4f9a;color:#2b4f9a}
.social-feed{border-color:#19a2c9;color:#19a2c9}
.social-video{border-color:#c4231d;color:#c4231d}
.footnav{position:absolute;top:226px;left:0;width:1200px;display:flex;justify-content:center;font-family:var(--bold);font-size:20px;color:#d9d9d9}
.footnav a{padding:0 20px}
.footnav a+a{border-left:2px solid #d9d9d9}
.legal{position:absolute;top:300px;left:60px;right:60px;display:flex;justify-content:space-between;font-size:12px;color:#777}
.legal nav a{margin-left:22px}
</style>
</head>
<body>

<div class="topbar">
  <svg width="16" height="16" viewBox="0 0 16 16"><circle cx="8" cy="8" r="7" fill="none" stroke="#c9c9c9" stroke-width="1.5"/><path d="M5.5 4.5l1.5 0 .8 2-1 .8a5 5 0 0 0 1.9 1.9l.8-1 2 .8v1.5c-3.5.5-6.8-2.8-6-6z" fill="#c9c9c9"/></svg>
  <span>0400 - 555 - 012</span>
</div>

<header class="brand">
  <span class="brand-mark"></span>
  <span class="brand-name">Rosa &amp; Ted's Roaming Farm</span>
</header>

<nav class="mainnav">
  <ul>
    <li class="is-active">HOME</li><li>ABOUT</li><li>ANIMALS</li><li>SHOW</li><li>LINKS</li><li>WILDLIFE RELOCATION</li>
  </ul>
</nav>

<section class="hero">
  <div class="hero-photo" role="img" aria-label="Photo of the farm's white travelling van parked on a suburban driveway"></div>
  <div class="hero-copy">
    <h1 class="hero-title">LOREM IPSUM<br>DOLOR SIT AMET</h1>
    <p class="hero-text">Lorem ipsum dolor sit amet, consectetur adipiscing elit. Aliquam non tincidunt arcu. Curabitur facilisis facilisis nisl, rutrum mollis eros elementum ut. Praesent ac leo vel magna condimentum tpat et et orci. Mauris diam ligula, finibus at felis sed, commodo lorem ipsum erat.</p>
    <a class="btn" href="#">GET MORE INFO</a>
  </div>
  <div class="dots"><span></span><span></span><span></span><span></span><span></span></div>
</section>

<h2 class="section-title" style="top:925px">ABOUT US</h2>
<p class="section-lead" style="top:996px">Aenean mattis sapien vel orci volutpat pretium. Nulla venenatis lectus rhoncus viverra aliquet. Pellentesque finibus ut risus vitae sollicitudin. sagittis vel luctus vitae, ornare sit amet magna.</p>

<div class="story-grid">
  <div class="story-photo" role="img" aria-label="Photo of a small possum being held in a family kitchen" style="background:linear-gradient(135deg,#6b5a3a,#c9a77a,#8a7a5a)"></div>
  <div class="story-text">Keeping Australian wildlife as pets is a wonderful hobby. But when you find your house is wall to wall cages and tanks, there's a wombat running through your bungalow, crickets and meal worms boxed in containers on your kitchen bench, a possum sits on your table and your child wonders past pushing a lizard in a dolls pram..... it's an obsession.</div>
  <div class="story-photo" role="img" aria-label="Photo of a handler holding a large python" style="background:linear-gradient(135deg,#3d4a2d,#9c8a6a,#5a5a42)"></div>
  <div class="story-text">Rosa and Ted's Roaming Farm became a business in 2011. The animals themselves have always been a big part of Rosa and Ted's life. Every kid (and grown up kid) in the neighbourhood knows that if you want to pat a dingo, watch a snake eat, hold a crocodile.....just go to Rosa and Ted's house.</div>
  <div class="story-text">The love of these animals, and the joy they feel when sharing what they've learned, shines through in every performance they give. Just ask a child who has been to one of their shows. They will excitedly tell you all about the animals, how they got to touch or hold certain ones, why they sleep all day, what funny things the animals did, which ones they liked and which ones freaked them out... the word "awesome" features a lot in their description.</div>
  <div class="story-photo" role="img" aria-label="Photo of children at a school event looking at a lizard" style="background:linear-gradient(135deg,#4a6a7a,#b8a48a,#6a5a4a)"></div>
  <div class="story-text">Rosa and Ted's Roaming Farm has done parties for schools, kindergartens, daycare centres, children's play centres, birthday parties and social groups. They hold all the licenses and insurances and have done all the training needed to make each event safe. Rosa holds a DSE wildlife demonstrators licence and has a huge knowledge of the animals (plus bugs and other scary things) that he talks about. More than anything else though, Rosa and Ted's Roaming Farm is all about fun.</div>
  <div class="story-photo" role="img" aria-label="Photo of a smiling child holding a small animal" style="background:linear-gradient(135deg,#5a5a62,#c49078,#7a6a5a)"></div>
</div>

<section class="donate-band">
  <p>Rosa and Ted love to introduce people to our precious wildlife and help them to love the animals just as much as they do. If you'd like to help Rosa and Ted keep up their good work you can send them a donation through FundTray. Every little bit counts!</p>
  <a class="btn" href="#">DONATE</a>
  <div class="pay-row"><span></span><span></span><span></span><span></span></div>
</section>

<h2 class="section-title" style="top:1870px">OUR ANIMALS FAMILY</h2>
<p class="section-lead" style="top:1944px;font-size:19px">A huge range of native animals with fully qualified skilled handlers to help you get the most from this experience. Great for birthday parties, kindergartens, schools and all public events. Based in Kestrel Vale, Victoria but travelling to a wide range of surrounding areas.</p>
<div class="slider-arrows">
  <span><svg width="14" height="12" viewBox="0 0 14 12"><path d="M13 6H2M6 1L1 6l5 5" stroke="#fff" stroke-width="2.4" fill="none"/></svg></span>
  <span><svg width="14" height="12" viewBox="0 0 14 12"><path d="M1 6h11M8 1l5 5-5 5" stroke="#fff" stroke-width="2.4" fill="none"/></svg></span>
</div>

<div class="animal-grid">
  <div class="animal-card" role="img" aria-label="Photo of a barn owl" style="background:linear-gradient(160deg,#3a2e24,#b09a7a,#4a3a2a)"><div class="shade"></div><div class="animal-name">THE<br>BARN OWL</div><a class="btn" href="#">view more</a></div>
  <div class="animal-card" role="img" aria-label="Photo of a dingo" style="background:linear-gradient(160deg,#5a3a1a,#c07a3a,#3a2a1a)"><div class="shade"></div><div class="animal-name">THE<br>DINGO</div><a class="btn" href="#">view more</a></div>
  <div class="animal-card" role="img" aria-label="Photo of an eastern snake necked turtle" style="background:linear-gradient(160deg,#2a3a3a,#6a7a6a,#2a2e2a)"><div class="shade"></div><div class="animal-name">THE EASTERN<br>SNAKE NECK TURTLE</div><a class="btn" href="#">view more</a></div>
  <div class="animal-card" role="img" aria-label="Photo of a blue tongue lizard" style="background:linear-gradient(160deg,#6a6a6a,#9a8a7a,#4a5a6a)"><div class="shade"></div><div class="animal-name">THE BLUE<br>TONGUE LIZARD</div><a class="btn" href="#">view more</a></div>
  <div class="animal-card" role="img" aria-label="Photo of a water dragon" style="background:linear-gradient(160deg,#3a4a2a,#8a8a5a,#2a3a22)"><div class="shade"></div><div class="animal-name">THE<br>WATER DRAGON</div><a class="btn" href="#">view more</a></div>
  <div class="animal-card" role="img" aria-label="Photo of a blue and gold macaw" style="background:linear-gradient(160deg,#2a5a8a,#d0a83a,#3a3a4a)"><div class="shade"></div><div class="animal-name">THE BLUE<br>AND GOLD MACAW</div><a class="btn" href="#">view more</a></div>
  <div class="animal-card" role="img" aria-label="Photo of a salt water crocodile" style="background:linear-gradient(160deg,#4a4a3a,#8a8a6a,#3a3a2a)"><div class="shade"></div><div class="animal-name">THE SALT<br>WATER CROCODILE</div><a class="btn" href="#">view more</a></div>
  <div class="animal-card" role="img" aria-label="Photo of a frill neck lizard" style="background:linear-gradient(160deg,#2a2a2a,#7a6a4a,#3a2e22)"><div class="shade"></div><div class="animal-name">THE FRILL<br>NECK LIZARD</div><a class="btn" href="#">view more</a></div>
</div>

<h2 class="section-title" style="top:2625px">WHAT WE DO ?</h2>
<p class="section-lead" style="top:2700px">Aenean mattis sapien vel orci volutpat pretium. Nulla venenati.</p>

<div class="service-list">
  <div class="service">
    <svg width="66" height="60" viewBox="0 0 66 60"><circle cx="14" cy="14" r="8" fill="var(--leaf)"/><circle cx="33" cy="11" r="9" fill="var(--leaf)"/><circle cx="52" cy="14" r="8" fill="var(--leaf)"/><path d="M2 40q0-16 12-16t12 16zM20 46q0-20 13-20t13 20zM40 40q0-16 12-16t12 16z" fill="var(--leaf)"/><rect x="2" y="44" width="62" height="14" rx="4" fill="var(--leaf)"/></svg>
    <h3>THE<br>SHOW</h3>
    <p>Pellentesque pharetra nunc at convallis pulvinar. Fusce id lectus risus, ac imperdiet ligula lorem bibendum dapibus commodo.</p>
    <a class="btn" href="#">LEARN MORE</a>
  </div>
  <div class="service">
    <svg width="66" height="60" viewBox="0 0 66 60"><path d="M22 52L48 14a9 9 0 0 0-14-10L10 40a6 6 0 0 0 9 8l22-32" stroke="var(--leaf)" stroke-width="6" fill="none" stroke-linecap="round"/></svg>
    <h3>PARTY<br>SUPPLIES</h3>
    <p>Pellentesque pharetra nunc at convallis pulvinar. Fusce id lectus risus, ac imperdiet ligula lorem bibendum dapibus commodo.</p>
    <a class="btn" href="#">LEARN MORE</a>
  </div>
  <div class="service">
    <svg width="66" height="60" viewBox="0 0 66 60"><circle cx="33" cy="30" r="27" fill="var(--leaf)"/><path d="M16 18q8 2 10 10t-6 12M38 8q-2 10 8 14t6 16M30 54q2-10 10-10" stroke="#fff" stroke-width="4" fill="none"/></svg>
    <h3>WILDLIFE<br>RELOCATION</h3>
    <p>Pellentesque pharetra nunc at convallis pulvinar. Fusce id lectus risus, ac imperdiet ligula lorem bibendum dapibus commodo.</p>
    <a class="btn" href="#">LEARN MORE</a>
  </div>
</div>

<section class="contact">
  <div class="contact-photo" role="img" aria-label="Photo of a handler presenting a lizard to an audience indoors"></div>
  <form class="contact-panel">
    <h2>CONTACT US</h2>
    <div class="field">your name *</div>
    <div class="field">your e-mail *</div>
    <div class="field"><span>subject</span><svg width="16" height="16" viewBox="0 0 16 16"><path d="M3 6l5 5 5-5" stroke="#eee" stroke-width="2" fill="none"/></svg></div>
    <div class="field message">message</div>
    <p class="note">* required</p>
    <a class="btn" href="#">SUBMIT</a>
  </form>
</section>

<footer class="site-footer">
  <div class="social">
    <a class="social-link social-page" href="#">PAGE</a>
    <a class="social-link social-feed" href="#">FEED</a>
    <a class="social-link social-video" href="#">VIDEO</a>
  </div>
  <nav class="footnav"><a>HOME</a><a>ABOUT</a><a>ANIMALS</a><a>SHOW</a><a>LINKS</a><a>WILDLIFE RELOCATION</a></nav>
  <div class="legal">
    <span>Copyright © 2015-2016 All rights reserved</span>
    <nav><a>Terms &amp; Conditions</a><a>Privacy Policy</a><a>Refund Policy</a></nav>
  </div>
</footer>

</body>
</html>
```